An innovative software company needs a business card!

We need a business card design for our new innovative software company. Please use the details for the business card provided in business card details section. We will use the business card paper like: https://www.plavex.com/us/products/nfc/business-cards-plus.html Our company name: kelvora We have already a logo and colors to use in business cards too ,

Target Market(s)

App & Sofware Development

Industry/Entity Type

Software

Contact Information for Business Card

Lukas Brenner, BSc.
Owner and Creative Superhero

Adress:
Tulpenweg 37/4/1809
A - 1100, Wien

Tel: +43 (0) 676 921 35 60
Email: lukas.brenner@kelvora.at
Web: www.kelvora.at

Requirements
Must have
• - Use our logo
Nice to have
• It would be nice to have a nice picture on the backside. (About apps, software, technicals or funy stuff) - Use our colors as in business card (optional)

```html
<!DOCTYPE html>
<html lang="en">
<head>
<meta charset="utf-8">
<title>kelvora business card</title>
<link rel="stylesheet" href="https://fonts.googleapis.com/css2?family=Montserrat:wght@800&family=Arimo:wght@400;700&display=swap">
<style>
  :root {
    --brand-blue: #1fa9d8;
    --paper: #ffffff;
    --ink-grey: #6d6d6d;
    --soft-grey: #b9b9b9;
    --backdrop: #2c2c2e;
  }
  * { box-sizing: border-box; margin: 0; padding: 0; }
  html, body { width: 1200px; height: 950px; overflow: hidden; }
  body { background: var(--backdrop); position: relative; font-family: "Arimo", Arial, sans-serif; }

  .card { position: absolute; width: 620px; height: 354px; border-radius: 3px; overflow: hidden; }

  /* back side */
  .card-back { left: 80px; top: 80px; background: var(--brand-blue); }
  .card-back .brand {
    position: absolute; left: 0; right: 0; top: 120px;
    display: flex; align-items: center; justify-content: center; gap: 16px;
  }
  .card-back .brand-dot { width: 40px; height: 40px; border-radius: 50%; background: var(--paper); }
  .card-back .brand-name {
    font-family: "Montserrat", sans-serif; font-weight: 800; font-size: 54px;
    color: var(--paper); letter-spacing: -1px; line-height: 1;
  }
  .card-back .web {
    position: absolute; left: 0; right: 0; bottom: 58px; text-align: center;
    color: var(--paper); font-size: 12px; letter-spacing: 6px;
  }

  /* front side */
  .card-front { left: 500px; top: 480px; background: var(--paper); }
  .card-front .accent {
    position: absolute; right: -24px; top: 84px; width: 48px; height: 48px;
    border-radius: 50%; background: var(--brand-blue);
  }
  .card-front .brand {
    position: absolute; left: 44px; top: 92px; display: flex; align-items: center; gap: 14px;
  }
  .card-front .brand-dot { width: 44px; height: 44px; border-radius: 50%; background: var(--brand-blue); }
  .card-front .brand-name {
    font-family: "Montserrat", sans-serif; font-weight: 800; font-size: 60px;
    color: var(--brand-blue); letter-spacing: -1px; line-height: 1;
  }
  .card-front .person { position: absolute; right: 44px; top: 142px; text-align: right; }
  .card-front .person-name { color: var(--brand-blue); font-size: 19px; font-weight: 400; letter-spacing: 0.5px; }
  .card-front .person-role { color: var(--soft-grey); font-size: 12px; letter-spacing: 1px; margin-top: 3px; }

  .card-front .address {
    position: absolute; left: 44px; top: 196px; color: var(--ink-grey);
    font-size: 13px; line-height: 17px; font-style: normal;
  }
  .card-front .contacts { position: absolute; left: 44px; top: 238px; list-style: none; }
  .card-front .contacts li {
    display: flex; align-items: center; gap: 10px; height: 19px;
    color: var(--ink-grey); font-size: 13px;
  }
  .card-front .contacts svg { width: 13px; height: 13px; fill: var(--brand-blue); flex: none; }
</style>
</head>
<body>

  <section class="card card-back" aria-label="Card back">
    <div class="brand">
      <span class="brand-dot"></span>
      <span class="brand-name">kelvora</span>
    </div>
    <p class="web">www.kelvora.at</p>
  </section>

  <section class="card card-front" aria-label="Card front">
    <span class="accent"></span>
    <div class="brand">
      <span class="brand-dot"></span>
      <span class="brand-name">kelvora</span>
    </div>

    <div class="person">
      <p class="person-name">LUKAS BRENNER</p>
      <p class="person-role">OWNER &amp; CREATIVE SUPERHERO</p>
    </div>

    <address class="address">
      Tulpenweg 37/4/1809<br>A - 1100, Wien
    </address>

    <ul class="contacts">
      <li>
        <svg viewBox="0 0 16 16" aria-hidden="true"><path d="M1 5c0-2 2-3 7-3s7 1 7 3v1h-4V5H5v1H1zM3 8h10l1 6H2zm5 1.5a2 2 0 1 0 0 4 2 2 0 0 0 0-4z"/></svg>
        <span>+43 (0) 676 921 35 60</span>
      </li>
      <li>
        <svg viewBox="0 0 16 16" aria-hidden="true"><path d="M4 0h8a1 1 0 0 1 1 1v14a1 1 0 0 1-1 1H4a1 1 0 0 1-1-1V1a1 1 0 0 1 1-1zm1 2v10h6V2zm3 11a1 1 0 1 0 0 2 1 1 0 0 0 0-2z"/></svg>
        <span>+43 (0) 1 947 26 18</span>
      </li>
      <li>
        <svg viewBox="0 0 16 16" aria-hidden="true"><path d="M4 0h8v5H4zM1 6h14v7h-3v3H4v-3H1zm4 5v3h6v-3z"/></svg>
        <span>+43 (0) 1 947 26 19</span>
      </li>
      <li>
        <svg viewBox="0 0 16 16" aria-hidden="true"><path d="M0 3h16v2L8 10 0 5zm0 4 8 5 8-5v6H0z"/></svg>
        <span>lukas.brenner@kelvora.at</span>
      </li>
      <li>
        <svg viewBox="0 0 16 16" aria-hidden="true"><path d="M8 0a8 8 0 1 0 0 16A8 8 0 0 0 8 0zm-1 2v2l2 2-2 2H4L2 6a6 6 0 0 1 5-4zm3 3 3 1a6 6 0 0 1-1 7l-2-2V8z"/></svg>
        <span>www.kelvora.at</span>
      </li>
    </ul>
  </section>

</body>
</html>
```